Business Card Re-Design for a Lighting Designer

I would like my business card re-designed. It is currently high gloss and they scratch too easily. I don not think the current design lends itself well to a matte finish. I have included the current design for reference along with our company logo.
Check out our website for current branding.
http://www.brenmoorastudio.example

Updates
Some of the top contenders are muslim and it is a holiday for them. I do not want to discriminate and would expect the same courtesy for holidays we celebrate.
Target Market(s)
Interior Designers, Architects
Contact Information for Business Card
Logo - Name, Title, Address, Telephone Number and Extension, Email
Font styles to use
Requirements
Must have
- All the information listed on the current business card. If you use Red, it needs to be the red from our logo.
Nice to have
- Vertical and Horizontal Designs will be entertained.
Should not have
- Requirements for a glossy finish...should not look too corporate since we are a design firm.

```html
<!DOCTYPE html>
<html lang="en">
<head>
<meta charset="utf-8">
<title>Bren Moora Studio — Business Card</title>
<link href="https://fonts.googleapis.com/css2?family=Poppins:wght@200;300;400;600&display=swap" rel="stylesheet">
<style>
  :root {
    --brand-red: #9b0000;
    --card-white: #ffffff;
    --card-charcoal: #232527;
    --ink-dark: #1e1e1e;
    --ink-light: #f4f4f4;
    --ink-muted: #6e6e6e;
    --backdrop: #e6e3de;
  }
  * { margin: 0; padding: 0; box-sizing: border-box; }
  html, body { width: 1200px; height: 1040px; overflow: hidden; }
  body {
    background: var(--backdrop);
    font-family: "Poppins", sans-serif;
    position: relative;
  }
  .card {
    position: absolute;
    left: 180px;
    width: 840px;
    height: 480px;
    overflow: hidden;
    box-shadow: 0 6px 18px rgba(0,0,0,0.18);
  }
  .card--front { top: 30px; background: var(--card-white); }
  .card--back { top: 530px; background: var(--card-charcoal); }

  .light-beam { position: absolute; inset: 0; }

  .brand-square {
    position: absolute;
    background: var(--brand-red);
  }
  .card--front .brand-square { left: 250px; top: 215px; width: 150px; height: 150px; }

  .brand-name {
    position: absolute;
    font-weight: 200;
    color: var(--ink-dark);
    line-height: 1;
    letter-spacing: 1px;
  }
  .card--front .brand-name {
    left: 250px; top: 385px;
    font-size: 40px;
  }
  .brand-name__sub {
    display: block;
    margin-top: 12px;
    font-size: 16px;
    font-weight: 300;
    letter-spacing: 18px;
    color: var(--ink-muted);
  }

  .contact {
    position: absolute;
    right: 48px;
    top: 36px;
    text-align: right;
    color: var(--ink-light);
  }
  .contact__name { font-size: 30px; font-weight: 600; letter-spacing: 0.5px; line-height: 1.1; }
  .contact__title { font-size: 22px; font-weight: 300; margin-bottom: 14px; }
  .contact__line { font-size: 17px; font-weight: 300; line-height: 1.35; }
  .contact__gap { height: 12px; }

  .card--back .brand-square { left: 360px; top: 120px; width: 120px; height: 120px; }
  .card--back .brand-name {
    left: 0; right: 0; top: 270px;
    text-align center;
    text-align: center;
    font-size: 34px;
    color: var(--ink-light);
  }
  .website {
    position: absolute;
    left: 48px; bottom: 36px;
    font-size: 17px;
    font-weight: 400;
    letter-spacing: 6px;
    color: var(--ink-light);
  }
</style>
</head>
<body>

  <section class="card card--front" aria-label="Card front">
    <svg class="light-beam" viewBox="0 0 840 480" aria-hidden="true">
      <polygon points="290,215 330,0 840,0 840,340 400,300" fill="var(--brand-red)"/>
    </svg>
    <div class="brand-square" aria-hidden="true"></div>
    <p class="brand-name">BREN MOORA STUDIO<span class="brand-name__sub">DESIGN</span></p>
    <div class="contact">
      <p class="contact__name">MARISOL QUENBY</p>
      <p class="contact__title">Principal</p>
      <p class="contact__line">512 Fernway commons</p>
      <p class="contact__line">Suite210 Harlow Ridge</p>
      <p class="contact__line">Ohio 40118 USA</p>
      <div class="contact__gap"></div>
      <p class="contact__line">555.014.2290x1</p>
      <p class="contact__line">marisol@brenmoorastudio.example</p>
      <p class="contact__line">brenmoorastudio.example</p>
    </div>
  </section>

  <section class="card card--back" aria-label="Card back">
    <div class="brand-square" aria-hidden="true"></div>
    <p class="brand-name">BREN MOORA STUDIO</p>
    <p class="website">WWW.BRENMOORASTUDIO.EXAMPLE</p>
  </section>

</body>
</html>
```